Quillmera

Business cards and core flute signage. The business is only in its infant as a 'market' business. I would like the name to be curved across the page in different colours with a bold line underneath finished with an exotic pen drawing the line. (Similar to pictures)
We are trying to reach all markets as they are designer pens and items are made as requested or they can select from already manufactured pens on display.
I have included some images of the actual pens that I make for inspiration, we are very open to your ideas and guidance if you have a specific design in mind.
If you would more pen photo options, please contact me with your email details.
Darren Talbiro
Pen Maker & Wood Turner
Ph. 0438 271 546
Target Market(s)
Generally professional customers who would use a pen for work on a daily basis
Industry/Entity Type
Business
Requirements
Must have
- Punchy and catchy styling
Nice to have
- One of my pens

```html
<!DOCTYPE html>
<html lang="en">
<head>
<meta charset="utf-8">
<title>Quillmera — Business Card</title>
<link rel="stylesheet" href="https://fonts.googleapis.com/css2?family=Uncial+Antiqua&family=Great+Vibes&family=Arimo:wght@400;700&display=swap">
<style>
  :root {
    --page: #ffffff;
    --parchment-light: #c79a45;
    --parchment-mid: #8f6424;
    --parchment-dark: #4a3112;
    --band-dark: #1c1a17;
    --band-edge: #2e2a24;
    --title-gold: #e0a72a;
    --text-light: #ffffff;
    --pen-ivory: #ece6da;
    --pen-orange: #c45a1f;
    --pen-silver: #b9ad93;
  }
  * { margin: 0; padding: 0; box-sizing: border-box; }
  html, body {
    width: 1200px;
    height: 886px;
    overflow: hidden;
    background: var(--page);
  }
  .canvas {
    position: relative;
    width: 1200px;
    height: 886px;
    background: var(--page);
  }
  .business-card {
    position: absolute;
    left: 148px;
    top: 170px;
    width: 852px;
    height: 511px;
    overflow: hidden;
    background: var(--parchment-mid);
  }
  .parchment-texture {
    position: absolute;
    inset: 0;
    background:
      radial-gradient(ellipse 60% 45% at 35% 28%, var(--parchment-light) 0%, transparent 70%),
      radial-gradient(ellipse 50% 40% at 20% 85%, var(--parchment-light) 0%, transparent 75%),
      linear-gradient(160deg, var(--parchment-dark) 0%, var(--parchment-mid) 45%, var(--parchment-dark) 100%);
  }
  .dark-band {
    position: absolute;
    left: 0;
    top: 0;
    width: 852px;
    height: 511px;
  }
  .brand-name {
    position: absolute;
    left: 30px;
    top: 80px;
    font-family: "Uncial Antiqua", serif;
    font-size: 78px;
    line-height: 1;
    color: var(--title-gold);
  }
  .contact-block {
    position: absolute;
    left: 0;
    top: 278px;
    width: 470px;
    text-align: center;
    color: var(--text-light);
  }
  .tagline {
    font-family: "Great Vibes", cursive;
    font-size: 40px;
    line-height: 1;
  }
  .maker-name {
    margin-top: 14px;
    font-family: "Arimo", sans-serif;
    font-weight: 700;
    font-size: 21px;
  }
  .phone {
    margin-top: 12px;
    font-family: "Arimo", sans-serif;
    font-size: 21px;
    display: inline-flex;
    align-items: center;
    gap: 4px;
  }
  .phone-icon { width: 17px; height: 20px; }
  .pen-showcase {
    position: absolute;
    left: 0;
    top: 0;
    width: 852px;
    height: 511px;
  }
</style>
</head>
<body>
<div class="canvas">
  <div class="business-card">
    <div class="parchment-texture" role="img" aria-label="Aged parchment texture in warm amber and brown tones"></div>

    <svg class="dark-band" viewBox="0 0 852 511" aria-hidden="true">
      <path d="M0 272 L60 266 L120 274 L190 262 L260 270 L330 258 L400 266 L470 254 L540 262 L600 250 L680 258 L760 246 L852 254
               L852 400 L780 408 L700 398 L620 410 L540 402 L460 414 L380 404 L300 416 L220 406 L140 418 L70 408 L0 416 Z"
            fill="var(--band-dark)" stroke="var(--band-edge)" stroke-width="3"/>
    </svg>

    <div class="brand-name">Quillmera</div>

    <div class="contact-block">
      <div class="tagline">Custom Handmade Pens</div>
      <div class="maker-name">Darren Talbiro</div>
      <div class="phone">
        <svg class="phone-icon" viewBox="0 0 24 24" aria-hidden="true">
          <path d="M7 2 L10 6 L8 9 Q9 13 13 16 L16 14 L20 17 L18 21 Q10 22 5 14 Q2 8 4 4 Z" fill="var(--text-light)"/>
        </svg>
        <span>0438 271 546</span>
      </div>
    </div>

    <svg class="pen-showcase" viewBox="0 0 852 511" role="img" aria-label="Photograph of two ornate handmade pens, one ivory and one orange with silver fittings, crossing the card diagonally">
      <defs>
        <linearGradient id="pen-ivory-fill" x1="0" y1="0" x2="1" y2="0">
          <stop offset="0" stop-color="var(--pen-silver)"/>
          <stop offset="0.5" stop-color="var(--pen-ivory)"/>
          <stop offset="1" stop-color="var(--pen-silver)"/>
        </linearGradient>
        <linearGradient id="pen-orange-fill" x1="0" y1="0" x2="1" y2="0">
          <stop offset="0" stop-color="var(--pen-orange)"/>
          <stop offset="0.55" stop-color="var(--pen-silver)"/>
          <stop offset="1" stop-color="#6f5a3c"/>
        </linearGradient>
      </defs>
      <polygon points="600,0 720,0 480,511 330,511" fill="url(#pen-ivory-fill)"/>
      <polygon points="720,0 852,0 852,300 600,511 480,511" fill="url(#pen-orange-fill)"/>
    </svg>
  </div>
</div>
</body>
</html>
```